Postcard Design - New Movers - Men only haircuts

Advertisement for "New Movers" into the local area. to try our hair curt facility. Our business is called Shearing Den; hair cuts for men and boys and can be found on FB using the words "Shearing Den, Pooler Georgia". Our décor is man cave.

```html
<!DOCTYPE html>
<html lang="en">
<head>
<meta charset="utf-8">
<title>Shearing Den – New in Town Postcard</title>
<link href="https://fonts.googleapis.com/css2?family=Passion+One:wght@400;700&family=Playfair+Display:ital,wght@1,500&family=Arimo:wght@400&family=Tinos:wght@400;700&family=Cormorant+SC:wght@700&display=swap" rel="stylesheet">
<style>
  :root {
    --page: #ffffff;
    --wood-dark: #b88a52;
    --wood-mid: #d2aa72;
    --wood-light: #f3e4c4;
    --wood-edge: #7a552d;
    --ink: #111111;
    --ink-brown: #2e1f10;
    --outline: #3b2814;
    --grey-text: #555555;
    --line: #8a8a8a;
    --back-tint: #f5f2ee;
  }
  * { margin: 0; padding: 0; box-sizing: border-box; }
  html, body { width: 749px; height: 1200px; overflow: hidden; background: var(--page); }
  .canvas { position: relative; width: 749px; height: 1200px; }

  /* Front */
  .card-front {
    position: absolute; left: 12px; top: 12px; width: 725px; height: 569px;
    overflow: hidden; box-shadow: 0 2px 6px rgba(0,0,0,.35);
    background: var(--wood-mid);
  }
  .plank { position: absolute; left: 0; width: 100%; border-bottom: 2px solid var(--wood-edge); }
  .plank-top { top: 0; height: 156px; background: linear-gradient(180deg, #c99a5e, var(--wood-mid) 60%, #c4965c); }
  .plank-light { top: 156px; height: 192px; background: linear-gradient(90deg, var(--wood-light), #fbf2de 45%, #ead3a8); border-top: 2px solid var(--wood-edge); }
  .plank-lower { top: 348px; height: 186px; background: linear-gradient(180deg, #d6ad74, var(--wood-dark) 70%, #c59a62); }
  .plank-base { top: 534px; height: 35px; background: linear-gradient(180deg, #c9a06a, #b48550); border-bottom: none; }

  .headline {
    position: absolute; left: 0; top: 30px; width: 100%; text-align: center;
    font-family: "Passion One", sans-serif; font-weight: 700; font-size: 118px; line-height: 1;
    color: #fff; letter-spacing: 2px;
    -webkit-text-stroke: 3px var(--outline); paint-order: stroke fill;
    text-shadow: 2px 3px 3px rgba(0,0,0,.35);
  }
  .brand-front {
    position: absolute; left: 0; top: 178px; width: 100%; text-align: center;
    font-family: "Playfair Display", serif; font-style: italic; font-weight: 500;
    font-size: 94px; line-height: 1; color: var(--ink);
  }
  .tagline-front {
    position: absolute; left: 0; top: 292px; width: 100%; text-align: center;
    font-family: "Arimo", sans-serif; font-size: 36px; color: var(--ink);
  }
  .photo {
    position: absolute; border: 4px solid #f7f1e6; box-shadow: 2px 3px 6px rgba(0,0,0,.45);
  }
  .photo-crowd { left: 28px; top: 356px; width: 264px; height: 184px; transform: rotate(-4deg);
    background: linear-gradient(135deg, #8c8f8a, #3f6b4c 55%, #cfc7bd); }
  .photo-kid { left: 548px; top: 350px; width: 170px; height: 192px; transform: rotate(3deg);
    background: linear-gradient(160deg, #e6e6e2, #c9c7c2 50%, #b8352c 80%, #6e6a66); }
  .promise {
    position: absolute; left: 292px; top: 378px; width: 212px; text-align: center;
    font-family: "Cormorant SC", serif; font-weight: 700; font-size: 33px; line-height: 42px;
    color: var(--ink-brown);
  }

  /* Back */
  .card-back {
    position: absolute; left: 12px; top: 612px; width: 725px; height: 576px;
    background: linear-gradient(180deg, #fbfaf8, var(--back-tint) 60%, #ebe6df);
    box-shadow: 0 2px 6px rgba(0,0,0,.35);
  }
  .brand-back {
    position: absolute; left: 22px; top: 26px;
    font-family: "Playfair Display", serif; font-style: italic; font-weight: 500;
    font-size: 38px; line-height: 1; color: var(--ink);
  }
  .info-block { position: absolute; left: 22px; top: 72px; width: 232px; text-align: center; }
  .tagline-back { font-family: "Arimo", sans-serif; font-size: 15px; color: var(--ink); }
  .hours { margin-top: 4px; font-family: "Tinos", serif; font-size: 17px; line-height: 22px; color: var(--grey-text); }
  .photo-team { position: absolute; left: 288px; top: 32px; width: 138px; height: 138px;
    border: 3px solid #eadfcc;
    background: linear-gradient(160deg, #e8e6e1, #b8b4ad 45%, #2f3f66 75%, #8d8780); }
  .stamp-box { position: absolute; left: 580px; top: 42px; width: 111px; height: 120px; border: 1px solid #777; background: #fff; }

  .rules { position: absolute; left: 22px; top: 190px; width: 340px; font-family: "Tinos", serif; color: var(--ink); }
  .rules-title { font-size: 21px; font-weight: 400; margin-bottom: 3px; }
  .rules-list { list-style: none; font-size: 13px; line-height: 16.8px; }
  .rules-list li { display: flex; }
  .rules-list .num { font-weight: 700; width: 16px; flex: none; }
  .rules-list .sub { display: block; padding-left: 12px; }
  .booking { margin-top: 10px; font-size: 15.5px; font-weight: 700; padding-left: 10px; }

  .address-line { position: absolute; left: 374px; width: 317px; height: 1px; background: var(--line); }
</style>
</head>
<body>
<div class="canvas">

  <section class="card-front">
    <div class="plank plank-top"></div>
    <div class="plank plank-light"></div>
    <div class="plank plank-lower"></div>
    <div class="plank plank-base"></div>

    <h1 class="headline">NEW IN TOWN</h1>
    <p class="brand-front">Shearing Den</p>
    <p class="tagline-front">Men and Boys Haircuts</p>

    <div class="photo photo-crowd" role="img" aria-label="Photo of a crowd of people in green shirts getting heads shaved at a community event"></div>
    <p class="promise">You receive<br>the best service<br>or it's free</p>
    <div class="photo photo-kid" role="img" aria-label="Photo of a barber cutting a young boy's hair while he sits in a red toy car chair"></div>
  </section>

  <section class="card-back">
    <p class="brand-back">Shearing Den</p>
    <div class="info-block">
      <p class="tagline-back">Men and Boys Haircuts</p>
      <p class="hours">Hours<br>Monday- Friday 10-7:30pm<br>Saturday 10-5PM</p>
    </div>
    <div class="photo-team" role="img" aria-label="Photo of the shop team standing with a boy and a costumed superhero"></div>
    <div class="stamp-box"></div>

    <div class="rules">
      <h2 class="rules-title">Shearing Den Rules</h2>
      <ol class="rules-list">
        <li><span class="num">1.</span><span>What happens in the Den stays in the Den</span></li>
        <li><span class="num">2.</span><span>Ask for what you want, subtle hints don't work.</span></li>
        <li><span class="num">3.</span><span>Men control the remote.</span></li>
        <li><span class="num">4.</span><span>No pony tails unless you are Waylon Briggs.</span></li>
        <li><span class="num">5.</span><span>Bacon is a food group (See our wall of Bacon).</span></li>
        <li><span class="num">6.</span><span>Every man needs a Man Cave or Garage Mahal<span class="sub">(see our man cave must have's to help).</span></span></li>
        <li><span class="num">7.</span><span>Whatever men say makes perfect sense.</span></li>
        <li><span class="num">8.</span><span>There is NO crying in the den.</span></li>
        <li><span class="num">9.</span><span>No diva's or damsel in distress.</span></li>
        <li><span class="num">10.</span><span>&nbsp;There will be a $10 charge for putting up with<span class="sub">grumpy, irritable, or just plain mean people.</span></span></li>
      </ol>
      <p class="booking">To book an appointment please call us</p>
    </div>

    <div class="address-line" style="top:246px"></div>
    <div class="address-line" style="top:306px"></div>
    <div class="address-line" style="top:366px"></div>
    <div class="address-line" style="top:426px"></div>
  </section>

</div>
</body>
</html>
```